Hi,
We are an accounting firm looking to upgrade the following:
Logo, letterhead, withcomp slips and maybe our business cards. I have attached our original letterhead (sample A) and a letterhead (SAmple B) which we like the design and layout, however I want to stick with the colours of our orginal letterhead (Sample A) but improve and modernise the look with other letter head (Sample B) I have attached both. On the footer of Sample A, we would like to remove the names of the directors but leave EST. 1985 we also want to add the QRT logo ABN and TAX AGENT logo as stated in Sample B , we would like to do a layout for the header similar to SAmple B however maybe a bit more structured.

```html
<!DOCTYPE html>
<html lang="en">
<head>
<meta charset="utf-8">
<title>Brentholm Accountants – Business Card</title>
<link rel="stylesheet" href="https://fonts.googleapis.com/css2?family=Montserrat:wght@500;600;700&display=swap">
<style>
  :root {
    --navy: #173a57;
    --blue: #247bc6;
    --logo-blue: #133f86;
    --ink: #1d1d1d;
    --text: #1f2a36;
    --icon: #1d4f8c;
    --paper: #ffffff;
    --backdrop: #d6d6d6;
    --badge-fill: #e3e8ee;
  }
  * { margin: 0; padding: 0; box-sizing: border-box; }
  html, body { width: 982px; height: 1200px; overflow: hidden; }
  body {
    background: var(--backdrop);
    font-family: "Montserrat", Arial, sans-serif;
    position: relative;
  }
  .card {
    position: absolute;
    left: 119px;
    width: 743px;
    height: 454px;
    background: var(--paper);
    overflow: hidden;
  }
  .card--front { top: 115px; }
  .card--back { top: 627px; }

  .footer-band {
    position: absolute;
    left: 0; bottom: 0;
    width: 743px; height: 39px;
  }
  .est {
    position: absolute;
    left: 372px; bottom: 0;
    height: 39px; line-height: 39px;
    transform: translateX(-50%);
    color: #fff;
    font-weight: 600;
    font-size: 19px;
    letter-spacing: 0.5px;
  }

  .wordmark__name {
    position: absolute;
    left: 183px; top: 150px;
    color: var(--logo-blue);
    font-weight: 700;
    font-size: 70px;
    line-height: 1;
    letter-spacing: -1.5px;
  }
  .wordmark__mark {
    position: absolute;
    left: 200px; top: 268px;
    width: 26px; height: 26px;
    background: var(--logo-blue);
  }
  .wordmark__sub {
    position: absolute;
    left: 277px; top: 256px;
    color: var(--ink);
    font-weight: 500;
    font-size: 42px;
    line-height: 1;
    letter-spacing: -0.5px;
  }

  .accent { position: absolute; left: 0; top: 0; }

  .contacts {
    position: absolute;
    left: 256px; top: 100px;
    list-style: none;
    color: var(--text);
    font-size: 20px;
    font-weight: 500;
  }
  .contacts li {
    display: flex; align-items: flex-start;
    line-height: 26px;
  }
  .contacts li + li { margin-top: 9px; }
  .contacts svg { width: 20px; height: 20px; margin-top: 3px; margin-right: 9px; flex: none; }
  .contacts .address { margin-top: 10px; }

  .badges {
    position: absolute;
    left: 259px; top: 328px;
    display: flex; align-items: center;
    gap: 15px;
  }
  .badge { display: block; background: var(--badge-fill); }
  .badge--wide { width: 138px; height: 59px; }
  .badge--mid { width: 104px; height: 59px; }
  .badge--round { width: 70px; height: 70px; border-radius: 50%; }
</style>
</head>
<body>

  <section class="card card--front" aria-label="Business card front">
    <span class="wordmark__name">Brentholm</span>
    <span class="wordmark__mark" aria-hidden="true"></span>
    <span class="wordmark__sub">Accountants</span>
    <svg class="footer-band" viewBox="0 0 743 39" aria-hidden="true">
      <polygon points="0,0 568,0 530,39 0,39" fill="var(--navy)"/>
      <polygon points="588,0 588,39 550,39" fill="var(--navy)"/>
      <rect x="588" y="0" width="155" height="39" fill="var(--blue)"/>
    </svg>
    <span class="est">EST. 1985</span>
  </section>

  <section class="card card--back" aria-label="Business card back">
    <svg class="accent" width="743" height="454" viewBox="0 0 743 454" aria-hidden="true">
      <polygon points="207,101 207,177 130,177" fill="var(--blue)"/>
      <rect x="130" y="189" width="77" height="230" fill="var(--navy)"/>
      <polygon points="0,415 568,415 530,454 0,454" fill="var(--navy)"/>
      <polygon points="588,415 588,454 550,454" fill="var(--navy)"/>
      <rect x="588" y="415" width="155" height="39" fill="var(--blue)"/>
    </svg>

    <ul class="contacts">
      <li>
        <svg viewBox="0 0 20 20" aria-hidden="true"><path d="M5 2 L8 2 L9 6 L7 8 C8 10.5 9.5 12 12 13 L14 11 L18 12 L18 15 C18 16.5 17 17 15.5 17 C9 16.5 3.5 11 3 4.5 C3 3 3.5 2 5 2 Z" fill="var(--icon)"/></svg>
        <span>+61 3 9000 1234</span>
      </li>
      <li>
        <svg viewBox="0 0 20 20" aria-hidden="true"><g fill="none" stroke="var(--icon)" stroke-width="1.6"><rect x="2" y="7" width="16" height="11"/><rect x="5" y="2" width="10" height="5"/><path d="M5 10v6M8 10v6M11 10v6M14 10v6"/></g></svg>
        <span>+61 3 9000 5678</span>
      </li>
      <li>
        <svg viewBox="0 0 20 20" aria-hidden="true"><rect x="2" y="5" width="16" height="11" fill="var(--icon)"/><path d="M2 5 L10 11 L18 5 M2 16 L8 10 M18 16 L12 10" stroke="#fff" stroke-width="1.3" fill="none"/></svg>
        <span>info@brentholm.com.au</span>
      </li>
      <li>
        <svg viewBox="0 0 20 20" aria-hidden="true"><g fill="none" stroke="var(--icon)" stroke-width="1.5"><circle cx="10" cy="10" r="7.5"/><ellipse cx="10" cy="10" rx="3.3" ry="7.5"/><path d="M2.5 10h15M4 6h12M4 14h12"/></g></svg>
        <span>www.brentholmaccountants.com.au</span>
      </li>
      <li class="address">
        <svg viewBox="0 0 20 20" aria-hidden="true"><path d="M10 19 C6 14 4 11 4 8 A6 6 0 0 1 16 8 C16 11 14 14 10 19 Z" fill="none" stroke="var(--icon)" stroke-width="2"/><circle cx="10" cy="8" r="2.2" fill="var(--icon)"/></svg>
        <span>Brentholm Pty Ltd, ABN 12 345 678 901<br>42 Fernlea Road Ashwood Vic. 3147</span>
      </li>
    </ul>

    <div class="badges">
      <span class="badge badge--wide" role="img" aria-label="QRT membership badge"></span>
      <span class="badge badge--mid" role="img" aria-label="Business listing badge"></span>
      <span class="badge badge--round" role="img" aria-label="Registered tax agent badge"></span>
    </div>
  </section>

</body>
</html>
```